Flyer Design for Dental Horizons

Hi everyone,
Just looking to create a double-sided full colour DL-sized (210mm x 99mm) flyer for a new dental practice called Dental Horizons. The flyers will be distributed in letterboxes (along with a fridge magnet stuck onto it) around the nearby suburbs (approx. 10 000 flyers will be printed and delivered).
We have already got a logo and a preliminary website design as attached, and we would like the design of the brochure to match this. We would like the attached information presented in a neat, tidy and eye-catching manner for the flyer, along with stock imagery where required. The flyer will be orientated vertically.
Details of the location and opening hours can be found at www.dentalhorizonsqx.com.au. Please ignore the logo used on this site as it is only temporary.
Industry/Entity Type
Dental
Requirements
Must have
- Brochure Content
(Please note that the intention of the bold items is to have them highlighted at the top of the flyer). Please use stock imagery as required and we can buy them once final.
Front of the flyer: (in any order you think best)
- (In Bold writing) SPECIAL OFFER: Free check-ups for all new patients – valued at $6o!*
- “New dentist now open!”
- Emergency appointments available – call now!
- Bring the kids to feed the fish in our marine tank!
- Intraoral cameras
- Dental Horizons Logo
- Call us now: 3611 4072 or book online at www.dentalhorizonsqx.com.au
Also, we would like the following terms and conditions for the special offers in small font:
“Item code 011 only. Valid for appointments attended before 30th April 2013. Not to be used in conjunction with any other offer.”
Back of the flyer: (in any order you think best)
- (In Bold writing) Line 1: Scared of Needles?
- (In Bold writing) Line 2 (maybe with picture in between?): Try our needle free injection today!*
- Dental Horizons Logo
- Our Location – address and picture
- Our phone number: 3611 4072 (please make this prominent)
- A QR code (we can supply this to you shortly)
- Opening hours
- Our website: www.dentalhorizonsqx.com.au
*suitable candidates only
The colours primarily used are blues and greys, so please don’t stray too far away from this colour scheme.

```html
<!DOCTYPE html>
<html lang="en">
<head>
<meta charset="utf-8">
<title>Dental Horizons DL Flyer</title>
<link href="https://fonts.googleapis.com/css2?family=Bebas+Neue&family=Open+Sans:wght@400;600;700;800&display=swap" rel="stylesheet">
<style>
:root{
  --backdrop:#767676;
  --paper:#f0f0f0;
  --navy:#1e2a4a;
  --teal:#60bcc3;
  --white:#ffffff;
  --ink:#333740;
  --muted:#55585e;
  --row-light:#f0f0f0;
}
*{margin:0;padding:0;box-sizing:border-box}
html,body{width:1200px;height:1168px;overflow:hidden;background:var(--backdrop)}
body{position:relative;font-family:"Open Sans",Arial,sans-serif;color:var(--ink)}
.flyer{position:absolute;top:92px;width:456px;height:965px;background:var(--paper);overflow:hidden;box-shadow:0 1px 4px rgba(0,0,0,.25)}
.flyer--front{left:98px}
.flyer--back{left:628px}
.photo{position:absolute;left:0;top:0;width:456px}
.photo--smile{height:438px;background:linear-gradient(160deg,#f1cdb8 0%,#e4a995 45%,#c98476 70%,#f3e1d6 100%)}
.photo--needle{height:319px;background:linear-gradient(120deg,#f4f4f4 0%,#e6e6e8 40%,#c9a18b 70%,#6b5447 100%)}

/* front */
.tagline-band{position:absolute;left:0;top:379px;width:322px;height:36px;background:var(--navy);color:var(--white);font-size:18px;line-height:36px;padding-left:32px}
.offer-band{position:absolute;left:0;top:439px;width:456px;height:69px;background:var(--navy);color:var(--white);font-weight:800;font-size:46px;line-height:69px;padding-left:22px;letter-spacing:.5px}
.price-band{position:absolute;left:0;top:508px;width:456px;height:98px;background:var(--teal);color:var(--white)}
.price-band__lead{position:absolute;left:22px;top:18px;font-family:"Bebas Neue",sans-serif;font-size:27px;line-height:32px;letter-spacing:.3px}
.price-band__value{position:absolute;left:255px;top:-6px;font-family:"Bebas Neue",sans-serif;font-size:130px;line-height:130px}
.exclaim{position:absolute;left:0;top:0}
.terms{position:absolute;left:0;top:606px;width:456px;height:56px;background:var(--navy);color:var(--white);font-size:12.5px;line-height:16px;text-align:center;padding-top:12px}
.features{position:absolute;left:30px;top:680px;list-style:none;font-size:16px;color:var(--muted)}
.features li{position:relative;padding-left:29px;height:29px;line-height:24px}
.features li::before{content:"";position:absolute;left:0;top:10px;width:5px;height:5px;border-radius:50%;background:var(--muted)}

/* brand & contact */
.brand{position:absolute;display:flex;align-items:center;gap:10px;color:var(--navy);font-weight:700;font-size:26px}
.brand__square{width:26px;height:26px;background:var(--navy)}
.contact{position:absolute;left:27px;color:var(--navy)}
.contact__label{font-size:13px;color:var(--muted);line-height:18px}
.contact__phone{font-size:27px;line-height:30px;margin-bottom:4px}
.contact__web{font-size:27px;line-height:30px}

/* back */
.headline-tab{position:absolute;left:0;top:319px;width:456px;height:62px}
.headline-tab__text{position:absolute;left:39px;top:10px;color:var(--white);font-size:33px;line-height:40px}
.promo{position:absolute;left:39px;top:398px;color:var(--navy);font-size:33px;line-height:39px;text-transform:uppercase}
.promo__note{position:absolute;left:43px;top:481px;font-size:13.5px;color:#222}
.hours{position:absolute;left:41px;top:515px;width:375px;border-collapse:collapse;font-size:13.5px}
.hours th{background:var(--navy);color:var(--white);text-align:left;font-weight:700;height:34px;padding-left:14px;letter-spacing:.5px}
.hours td{height:26px;color:var(--muted)}
.hours td:first-child{padding-left:15px;width:105px}
.hours tr.is-dark td{background:var(--navy);color:var(--white)}
.address{position:absolute;left:42px;top:793px;font-size:13.5px;line-height:17px;color:var(--ink)}
</style>
</head>
<body>

<section class="flyer flyer--front">
  <div class="photo photo--smile" role="img" aria-label="Close-up stock photo of a smiling woman with bright white teeth"></div>
  <div class="tagline-band">“NEW DENTIST NOW OPEN!”</div>
  <div class="offer-band">SPECIAL OFFER</div>
  <div class="price-band">
    <div class="price-band__lead">FREE CHECK-UPS FOR ALL<br>NEW PATIENTS VALUED AT</div>
    <div class="price-band__value">$60</div>
  </div>
  <svg class="exclaim" width="456" height="620" viewBox="0 0 456 620" aria-hidden="true">
    <polygon points="412,460 438,460 412,568 399,568" fill="#ffffff"/>
    <polygon points="399,578 414,578 410,598 395,598" fill="#ffffff"/>
  </svg>
  <div class="terms">“Item code 011 only. Valid for appointments attended before<br><strong>30th April 2013</strong>. Not to be used in conjunction with any other offer.”</div>
  <ul class="features">
    <li>Emergency appointments available – call now!</li>
    <li>Bring the kids to feed the fish in our marine tank!</li>
    <li>Intraoral cameras</li>
  </ul>
  <div class="brand" style="left:30px;top:796px"><span class="brand__square"></span>Dental Horizons</div>
  <div class="contact" style="top:850px">
    <div class="contact__label">Call us now:</div>
    <div class="contact__phone">3611 4072</div>
    <div class="contact__label">or book online at</div>
    <div class="contact__web">www.dentalhorizonsqx.com.au</div>
  </div>
</section>

<section class="flyer flyer--back">
  <div class="photo photo--needle" role="img" aria-label="Stock photo of a nervous patient at the dentist with a syringe held near"></div>
  <div class="headline-tab">
    <svg width="456" height="62" viewBox="0 0 456 62" aria-hidden="true">
      <rect x="0" y="0" width="456" height="5" fill="#1e2a4a"/>
      <polygon points="0,0 372,0 316,62 0,62" fill="#1e2a4a"/>
    </svg>
    <div class="headline-tab__text">Scared of Needles?</div>
  </div>
  <div class="promo">Try our needle free<br>injection today!*</div>
  <div class="promo__note">*suitable candidates only</div>
  <table class="hours">
    <thead><tr><th colspan="2">OPENING HOURS</th></tr></thead>
    <tbody>
      <tr><td>Monday</td><td>8:00 am – 8:00 pm</td></tr>
      <tr class="is-dark"><td>Tuesday</td><td>8:00 am – 8:00 pm</td></tr>
      <tr><td>Wednesday</td><td>8:00 am – 8:00 pm</td></tr>
      <tr class="is-dark"><td>Thursday</td><td>8:00 am – 8:00 pm</td></tr>
      <tr><td>Friday</td><td>8:00 am – 5:30 pm</td></tr>
      <tr class="is-dark"><td>Saturday</td><td>9:00 am – 2:00 pm</td></tr>
    </tbody>
  </table>
  <div class="brand" style="left:42px;top:738px"><span class="brand__square"></span>Dental Horizons</div>
  <div class="address">1420-1436 Kestrel Ridge Rd, Parkview Shopping Centre,<br>Ashgrove Heights, Queensland, 4199</div>
  <div class="contact" style="left:41px;top:841px">
    <div class="contact__label">Call us now:</div>
    <div class="contact__phone">3611 4072</div>
    <div class="contact__label">or book online at</div>
    <div class="contact__web">www.dentalhorizonsqx.com.au</div>
  </div>
</section>

</body>
</html>
```